Cover Art Design for a Notebook

We are going to give away some note books to our marketing department and want an elegant art design for the cover. There is a theme centered around ABCD of marketing that we want to leverage in the design. So these letters should be prominent in the design. The ABCD stand for Agility, Boost, Customer, Data.

If you could Cleverly incorporate these words into the letters with a good design that would be good.

But please make the ABCD the focus of the artwork. The words associated with them should be subtle, in the background, visible but not the focus.

We are looking for stylish. We want people to feel proud of the ELEGANT DESIGN when they take out this notebook for business.

Also worth mentioning- We are a biotechnology company so if you incorporate elements in that theme in, on, or around the ABCD letters, it could be a good idea. As long as it doesn’t kill the rest of the design.

I will upload our logo for Lumera Vantide Biologic later (you can see it online) and this will need to go in one corner.

Notebook will be A5 format. Image on front cover only. Need ASAP.

(Do not make baby blocks as we don’t want something that looks like a kids book)

Target Market(s)

business people who feel proud to pull out this notebook

Industry/Entity Type

Biotechnology

Colors
ec1f27
ffffff
000000

Requirements
Must have
• ELEGANT ART DESIGN USING ABCD
Nice to have
• see brief above
Should not have
• baby blocks

```html
<!DOCTYPE html>
<html lang="en">
<head>
<meta charset="utf-8">
<title>ABCD of Marketing – Notebook Cover</title>
<link rel="stylesheet" href="https://fonts.googleapis.com/css2?family=EB+Garamond:wght@400&family=Pinyon+Script&display=swap">
<style>
  :root {
    --page: #ffffff;
    --cover: #000000;
    --silver-dark: #5e5f62;
    --silver-mid: #a9aaad;
    --silver-light: #ffffff;
    --gold: #c8924c;
  }
  html, body {
    margin: 0;
    padding: 0;
    width: 1200px;
    height: 1200px;
    overflow: hidden;
    background: var(--page);
  }
  .canvas {
    position: relative;
    width: 1200px;
    height: 1200px;
    background: var(--page);
  }
  .cover {
    position: absolute;
    left: 207px;
    top: 33px;
    width: 796px;
    height: 1126px;
    background: var(--cover);
    overflow: hidden;
  }
  .cover-art {
    display: block;
    width: 796px;
    height: 1126px;
  }
  .initial {
    font-family: "EB Garamond", "Garamond", serif;
    font-size: 450px;
    font-weight: 400;
    fill: url(#silver);
  }
  .keyword {
    font-family: "Pinyon Script", cursive;
    font-size: 42px;
    letter-spacing: 7px;
    fill: var(--gold);
  }
</style>
</head>
<body>
  <main class="canvas">
    <section class="cover" aria-label="ABCD of Marketing notebook cover">
      <svg class="cover-art" viewBox="0 0 796 1126" xmlns="http://www.w3.org/2000/svg">
        <defs>
          <linearGradient id="silver" gradientUnits="userSpaceOnUse" x1="0" y1="40" x2="620" y2="1100">
            <stop offset="0" stop-color="var(--silver-dark)" style="stop-color:#5e5f62"/>
            <stop offset="0.5" stop-color="#a9aaad"/>
            <stop offset="1" stop-color="#ffffff"/>
          </linearGradient>
        </defs>

        <text class="initial initial-a" x="31" y="335">A</text>
        <text class="initial initial-b" x="250" y="618">B</text>
        <text class="initial initial-c" x="318" y="807">C</text>
        <text class="initial initial-d" x="470" y="1087">D</text>

        <text class="keyword keyword-agility" x="222" y="186">Agility</text>
        <text class="keyword keyword-boost" x="399" y="407">Boost</text>
        <text class="keyword keyword-customer" x="410" y="683">Customer</text>
        <text class="keyword keyword-data" x="561" y="952">Data</text>
      </svg>
    </section>
  </main>
</body>
</html>
```